Talvane Salmon Labels

We need a graphic design label for a new product launch. Talvane is an 100% Australian family business specialised in making marinades made from natural and locally sourced fresh ingredients for fish and seafood. We make remarkable food for fine cooking prepared by hand at our kitchen in Condell Park, using the same ingredients and techniques you would use at home.

We are planning to launch three marinades for salmon.
The flavours are:

- Herb, Lemon & Cracked Black Pepper
- Ginger, Honey & Soy
- Coriander, Lemongrass, Shallot and Ginger

The marinades will be packed in a 300 grams clear pouch with spout and sold in the seafood section of a major retail supermarket.

Measurements of the pouch: 140 mm wide and 210 mm high but only 160 mm high from the spout downwards.

Label: For the label, It will be a 120mm wide X 120mm high If not slightly smaller. Please refer to File 2: to see the pouch.

The label will cover 75% of the front of the pouch and the marinade itself will be visible in the remaining 25 % of the pouch. The colours of the marinades are green for Herb, Lemon & Cracked Black Pepper and Coriander, Lemongrass, Shallot and Ginger; and dark brown for Ginger, Honey & Soy.

Our marinades do not contain additives. The marinades are Gluten free.

The label needs to visually communicate that the marinade is used for salmon.

Please choose a suitable typography for our name Talvane that communicates an artisan feel.

Please refer to File 1 as a guide to what we would like, but keep in mind we are very open to any ideas you may have.

Colours should reflect the nature of our business, as outlined above.
Updates

Hello Designers,

This is what the actual pouch looks like https://www.filecrate.example/sc/4kd82mz19qp0x/Tq73Lowm8_

We would like the label to be roughly 120mm X 120mm or within those parameters to fit the packaging.

Thank you!
- Miriam

Hey Designers,

we have been looking at your designs and while we have liked some elements of them we would like to see more creativity with the actual graphics and shapes of the labels, different colour contrast and more clever and quirky designs. We want to make fish fun and interesting to consumers, something rustic that catches the eye but at the same time is still sophisticated and upmarket. 

We would like to see the following on your packaging designs:

- Pastels colours (green, blue and yellow).
- The 'Talvane gourmet' font to be in bolder typography
- An ink looking stamp for 'gluten free, no additives'
- Something about the product being hand crafted
- Must include the following text: Marinades made from natural and locally sourced fresh ingredients for fish and seafood

here are some examples for you to be inspired by

Some font ideas ..

http://pinboardly.example/pin/501928374650192837/
http://pinboardly.example/pin/73019284756102938/
http://pinboardly.example/pin/618293047561829304/
http://pinboardly.example/pin/339201847562019384/
http://pinboardly.example/pin/447102938475610293/
http://pinboardly.example/pin/582019374651029384/

colours/images/graphics

http://pinboardly.example/pin/194820375619203847/
http://pinboardly.example/pin/730192846501928374/
http://pinboardly.example/pin/865019283746501927/
http://pinboardly.example/pin/412093847561029384/ (We like this concept) 

Good luck! 

 

Target Market(s)

Home cooks, young professionals, anyone with a healthy eating lifestyle.

Industry/Entity Type

Graphic Design

Requirements
Must have
• The label needs to visually communicate that the marinade is used for salmon.
- Include "Gluten Free" and "No Additives" on the label
- Outline the freshness of the ingredients used in the marinade eg. Coriander, Lemongrass, Shallot and Ginger to be included on the label.
- Bright and eye catching colours (food friendly colours).
Nice to have
• - Open to pastel colours
- Vector drawings
Should not have
• - dull colours

```html
<!DOCTYPE html>
<html lang="en">
<head>
<meta charset="utf-8">
<title>Talvane Salmon Marinade – Pouch Label</title>
<link rel="stylesheet" href="https://fonts.googleapis.com/css2?family=Delius&family=Open+Sans:wght@400;600;700&display=swap">
<style>
  :root {
    --backdrop: #eef3d6;
    --pouch-green: #3f8f1c;
    --pouch-green-light: #5cb52a;
    --panel-dark: #1c1c1c;
    --panel-mid: #3a3a3a;
    --silver: #b9b9b9;
    --silver-light: #e6e6e6;
    --title-green: #c8e07c;
    --herb-green: #86ac2c;
    --herb-dark: #4f6e14;
    --salmon: #f07a2a;
    --salmon-light: #ffab6a;
    --slate: #3b3127;
    --white: #ffffff;
  }
  html, body {
    margin: 0;
    width: 1200px;
    height: 960px;
    overflow: hidden;
    background: var(--backdrop);
  }
  .canvas { display: block; width: 1200px; height: 960px; }
  .brand-name { font-family: "Delius", cursive; font-size: 62px; fill: var(--silver-light); }
  .brand-origin { font-family: "Open Sans", sans-serif; font-weight: 700; font-size: 17px; fill: var(--white); letter-spacing: 0.5px; }
  .ingredient-promise { font-family: "Open Sans", sans-serif; font-weight: 600; font-size: 14px; fill: var(--silver-light); }
  .product-title { font-family: "Delius", cursive; font-size: 64px; fill: var(--title-green); }
  .flavour-line { font-family: "Open Sans", sans-serif; font-weight: 700; font-size: 19px; fill: var(--silver-light); }
  .dietary-note { font-family: "Open Sans", sans-serif; font-size: 23px; fill: var(--white); }
  .dietary-band { fill: var(--slate); opacity: 0.85; }
</style>
</head>
<body>
<svg class="canvas" viewBox="0 0 1200 960" xmlns="http://www.w3.org/2000/svg">
  <defs>
    <linearGradient id="pouchGreen" x1="0" x2="1">
      <stop offset="0" stop-color="var(--pouch-green)"/>
      <stop offset="0.5" stop-color="var(--pouch-green-light)"/>
      <stop offset="1" stop-color="var(--pouch-green)"/>
    </linearGradient>
    <linearGradient id="panelDark" x1="0" y1="0" x2="0" y2="1">
      <stop offset="0" stop-color="var(--panel-mid)"/>
      <stop offset="0.5" stop-color="var(--panel-dark)"/>
      <stop offset="1" stop-color="var(--panel-mid)"/>
    </linearGradient>
    <linearGradient id="ribbonFill" x1="0" y1="0" x2="0" y2="1">
      <stop offset="0" stop-color="#4a4a4a"/>
      <stop offset="1" stop-color="#161616"/>
    </linearGradient>
    <radialGradient id="herbFill" cx="0.5" cy="0.45" r="0.6">
      <stop offset="0" stop-color="var(--herb-green)"/>
      <stop offset="1" stop-color="var(--herb-dark)"/>
    </radialGradient>
    <linearGradient id="salmonScene" x1="0" y1="0" x2="0.3" y2="1">
      <stop offset="0" stop-color="var(--slate)"/>
      <stop offset="0.3" stop-color="var(--salmon-light)"/>
      <stop offset="0.65" stop-color="var(--salmon)"/>
      <stop offset="0.85" stop-color="var(--slate)"/>
    </linearGradient>
    <filter id="titleGlow" x="-20%" y="-20%" width="140%" height="140%">
      <feGaussianBlur stdDeviation="3" result="b"/>
      <feMerge><feMergeNode in="b"/><feMergeNode in="SourceGraphic"/></feMerge>
    </filter>
    <path id="flavourArc" d="M 418 520 Q 560 650 780 560"/>
  </defs>

  <g class="pouch">
    <path class="pouch-body" d="M 365 48 H 812 V 360 L 806 860 Q 590 872 384 860 L 372 360 Z" fill="url(#pouchGreen)"/>
    <path class="pouch-panel" d="M 403 52 H 774 V 840 H 414 Z" fill="url(#panelDark)" stroke="var(--silver)" stroke-width="4"/>

    <rect class="salmon-photo" role="img" aria-label="Photo of fresh raw salmon fillets on a dark slate board" x="418" y="590" width="350" height="246" fill="url(#salmonScene)"/>

    <g class="ingredient-promise-group">
      <text class="ingredient-promise" x="590" y="90" text-anchor="middle">Marinades made from natural and locally sourced</text>
      <text class="ingredient-promise" x="590" y="110" text-anchor="middle">fresh ingredients for fish and seafood</text>
    </g>

    <g class="brand-ribbon">
      <path d="M 388 170 Q 390 140 420 140 H 770 Q 798 140 796 170 L 792 210 Q 780 232 770 242 L 760 200 H 420 L 404 242 Q 392 230 390 210 Z" fill="url(#ribbonFill)" stroke="var(--silver)" stroke-width="2"/>
      <text class="brand-name" x="590" y="192" text-anchor="middle">Talvane</text>
      <text class="brand-origin" x="590" y="220" text-anchor="middle">AUSTRALIAN MADE</text>
    </g>

    <g class="product-title-group" filter="url(#titleGlow)">
      <text class="product-title" x="580" y="298" text-anchor="middle">Salmon</text>
      <text class="product-title" x="598" y="366" text-anchor="middle">Marinade</text>
    </g>

    <g class="flavour-window" transform="rotate(-7 590 500)">
      <ellipse cx="590" cy="500" rx="214" ry="110" fill="#111" stroke="var(--silver)" stroke-width="4"/>
      <ellipse class="marinade-texture" role="img" aria-label="Close-up texture of green herb marinade" cx="590" cy="495" rx="196" ry="92" fill="url(#herbFill)" stroke="var(--herb-dark)" stroke-width="2"/>
    </g>
    <text class="flavour-line"><textPath href="#flavourArc" startOffset="50%" text-anchor="middle">Herb, Lemon &amp; Cracked Black Pepper</textPath></text>

    <rect class="dietary-band" x="418" y="772" width="270" height="64"/>
    <text class="dietary-note" x="553" y="798" text-anchor="middle">No Additives</text>
    <text class="dietary-note" x="553" y="826" text-anchor="middle">Gluten Free</text>
    <circle class="certification-badge" cx="732" cy="804" r="30" fill="none" stroke="var(--pouch-green-light)" stroke-width="4"/>
  </g>
</svg>
</body>
</html>
```